Gentle Kundalini Yoga with Gong Relaxation

I teach a gentle Kundalini Yoga class with Gong relaxation every Thursday morning from 8:30-10am at the Ashford Meadows Unity Chapel 17 Garber Lane Pellam Crest. This class is unique in that I play the gong for an extended relaxation. Gongs are generally only found in established Yoga centers not in a small neighborhood yoga class. I am trying to grow this class from a current class size of 5 students. I would like to double the class size.
Updates
Project Deadline Extended
Reason: We had a blizzard on January 27 and 28 in the Boston area and I was too busy removing snow to tend to the postcard design-Thank you-Dora Fitchley
Industry/Entity Type
Church

```html
<!DOCTYPE html>
<html lang="en">
<head>
<meta charset="utf-8">
<title>Gentle Kundalini Yoga with Gong Relaxation</title>
<link rel="stylesheet" href="https://fonts.googleapis.com/css2?family=Arimo:wght@400;700&display=swap">
<style>
  :root {
    --white: #ffffff;
    --lime: #d9f25e;
    --price-green: #c6f07c;
    --deep-green: #1f4a14;
    --mid-green: #4f8a2a;
    --bright-green: #86b83c;
    --moss: #2f5e1c;
    --band: rgba(20, 28, 22, 0.55);
  }
  * { margin: 0; padding: 0; box-sizing: border-box; }
  html, body { width: 1200px; height: 613px; overflow: hidden; background: #ffffff; }
  .card {
    position: relative;
    width: 1200px;
    height: 613px;
    overflow: hidden;
    font-family: "Arimo", Arial, sans-serif;
  }
  .backdrop {
    position: absolute;
    inset: 0;
    background:
      radial-gradient(ellipse at 80% 45%, #1d6b2a 0%, rgba(29,107,42,0) 45%),
      radial-gradient(ellipse at 30% 30%, var(--bright-green) 0%, rgba(134,184,60,0) 55%),
      radial-gradient(ellipse at 55% 65%, #a8c860 0%, rgba(168,200,96,0) 40%),
      linear-gradient(180deg, var(--mid-green) 0%, var(--moss) 70%, #3d5a3a 100%);
  }
  .title {
    position: absolute;
    left: 30px;
    top: 42px;
    color: var(--white);
    font-size: 62px;
    font-weight: 400;
    line-height: 70px;
    letter-spacing: -0.5px;
  }
  .rule {
    position: absolute;
    left: 5px;
    top: 238px;
    width: 381px;
    height: 5px;
    background: var(--white);
  }
  .schedule {
    position: absolute;
    left: 152px;
    top: 303px;
    color: var(--white);
    font-size: 50px;
    line-height: 60px;
    letter-spacing: 2px;
  }
  .price {
    position: absolute;
    left: 156px;
    top: 466px;
    color: var(--price-green);
    font-size: 27px;
    letter-spacing: 0.5px;
  }
  .info-band {
    position: absolute;
    left: 0;
    top: 510px;
    width: 1200px;
    height: 88px;
    background: var(--band);
  }
  .venue {
    position: absolute;
    left: 48px;
    top: 516px;
    width: 668px;
    color: var(--lime);
    font-size: 26px;
    line-height: 24px;
    text-align: center;
  }
  .contact {
    position: absolute;
    left: 820px;
    top: 522px;
    width: 330px;
    color: var(--lime);
    font-size: 28px;
    line-height: 30px;
    text-align: center;
    letter-spacing: 0.5px;
  }
</style>
</head>
<body>
  <main class="card">
    <div class="backdrop" role="img" aria-label="Photograph of a woman in a green top seated cross-legged in meditation with a mudra hand, beside calm water in front of softly blurred green foliage"></div>

    <h1 class="title">Gentle Kundalini Yoga<br>with Gong Relaxation</h1>
    <div class="rule"></div>

    <p class="schedule">Thursdays<br>8:30-10am</p>

    <p class="price">$12.00 a class or a 10 class card for $100.00</p>

    <div class="info-band"></div>
    <p class="venue">Ashford Meadows Unity Chapel<br>17 Garber Lane Pellam Crest,<br>Massachussetts</p>
    <p class="contact">contact<br>555-014-2280</p>
  </main>
</body>
</html>
```